Quillory Points website re-design and

the institute of massage therapy is ready for a new website. The current website is around 12 years old and it looks old. Luckily the clients is not against changing the colors so the new design does not have to use the current ugly green color scheme. Be creative! Make it pretty, modern and inviting. The current colors look like mold. Nobody likes mold. I have attached the logo asset file as well as a txt document that details the new website design parameters

1 page

```html
<!DOCTYPE html>
<html lang="en">
<head>
<meta charset="utf-8">
<title>Quillory Points – Massage Therapy Continuing Education</title>
<link href="https://fonts.googleapis.com/css2?family=Yanone+Kaffeesatz:wght@400;500&family=Montserrat:wght@400;500;600&display=swap" rel="stylesheet">
<style>
:root{
  --purple:#8f3a97;
  --purple-dark:#6e2a76;
  --pink:#fbe2e1;
  --pink-soft:#fdf1f1;
  --lilac:#fbe9fb;
  --ink:#222;
  --grey:#6d6d6d;
  --bar:#2c2c2c;
  --footer:#3b3b3b;
  --white:#fff;
}
*{box-sizing:border-box;margin:0;padding:0}
html,body{width:1200px;height:5110px;overflow:hidden;background:var(--white)}
body{font-family:"Montserrat",sans-serif;color:var(--ink);position:relative}
.abs{position:absolute}
.display{font-family:"Yanone Kaffeesatz",sans-serif;font-weight:400;color:var(--ink)}

/* top bar */
.topbar{left:0;top:0;width:1200px;height:28px;background:var(--bar);color:#ddd;font-size:12px}
.topbar span{position:absolute;top:7px}
.topbar .sep{width:1px;height:12px;background:#777;top:8px}

/* nav */
.nav{left:0;top:28px;width:1200px;height:76px;background:var(--white)}
.brand{display:flex;align-items:center;gap:10px}
.brand-dot{width:26px;height:26px;border-radius:50%;background:var(--purple)}
.brand-name{font-family:"Montserrat",sans-serif;font-weight:500;font-size:17px;letter-spacing:2px;color:var(--purple-dark);text-transform:uppercase}
.nav .brand{position:absolute;left:105px;top:24px}
.nav-link{position:absolute;top:30px;font-size:15px;color:#333}
.nav-link.active::after{content:"";position:absolute;left:0;right:0;bottom:-10px;height:2px;background:#333}
.btn-outline{position:absolute;left:872px;top:19px;width:139px;height:42px;border:1.5px solid var(--purple);border-radius:21px;font-size:15px;text-align:center;line-height:39px;color:#333}
.cart{position:absolute;left:1063px;top:26px;width:28px;height:28px;border-radius:50%;background:var(--pink)}

/* hero */
.hero{left:0;top:104px;width:1200px;height:554px;background:var(--pink);overflow:hidden}
.hero-kicker{left:105px;top:140px;font-size:22px;color:var(--purple)}
.hero-title{left:103px;top:168px;font-size:64px;line-height:64px}
.search-label{left:105px;top:388px;font-size:20px;color:#333}
.search{left:105px;top:431px;width:988px;height:60px;display:flex;gap:8px}
.field{background:var(--white);border-radius:30px;height:60px;font-size:16px;color:var(--purple);display:flex;align-items:center;padding-left:70px;border:1px solid #eccfe0}
.field.keyword{width:386px}
.field.hours{width:370px;padding-left:28px;justify-content:space-between;padding-right:18px}
.chev{width:26px;height:26px;border-radius:50%;background:var(--pink);display:flex;align-items:center;justify-content:center}
.btn-search{width:218px;height:60px;border-radius:30px;background:var(--purple);color:#fff;font-size:16px;font-weight:500;text-align:center;line-height:60px}

/* section headings */
.sec-title{width:1200px;left:0;text-align:center;font-size:46px}
.divider{left:470px;width:260px;height:20px}
.divider::before,.divider::after{content:"";position:absolute;top:9px;width:105px;height:1.5px;background:var(--purple)}
.divider::before{left:0}.divider::after{right:0}
.divider i{position:absolute;left:120px;top:0;width:20px;height:20px;border-radius:50%;background:var(--purple)}

/* packages */
.pkg{width:312px;height:435px;top:888px;border:1px solid #eee;border-radius:156px 156px 4px 4px;background:#fff;text-align:center}
.pkg-photo{position:absolute;left:6px;top:6px;width:298px;height:206px;border-radius:150px 150px 0 0}
.pkg-icon{position:absolute;left:120px;top:178px;width:70px;height:70px;border-radius:50%;background:var(--purple);border:5px solid #fff}
.pkg-icon::after{content:"";position:absolute;left:18px;top:18px;width:24px;height:24px;border:3px solid #fff;border-radius:50%}
.pkg h3{position:absolute;left:0;right:0;top:266px;font-weight:400;font-size:22px}
.pkg p{position:absolute;left:20px;right:20px;top:304px;font-size:12px;line-height:20px;color:#555}
.pkg .more{position:absolute;left:82px;top:384px;width:146px;height:36px;border-radius:18px;background:var(--pink-soft);font-size:13px;color:var(--purple);line-height:36px}

/* free course band */
.band{left:0;top:1418px;width:1200px;height:577px;overflow:hidden}
.band-title{left:684px;top:1640px;font-size:48px}
.band-title em{font-style:normal;color:var(--purple)}
.band-sub{left:684px;top:1715px;width:400px;font-size:20px;line-height:30px;color:#666}
.btn{border-radius:30px;background:var(--purple);color:#fff;text-align:center;font-weight:500}
.band-btn{left:678px;top:1810px;width:224px;height:58px;line-height:58px;font-size:16px}

/* reasons */
.kicker{left:0;width:1200px;text-align:center;font-size:15px;color:var(--purple)}
.timeline{left:600px;top:2425px;width:0;height:1115px;border-left:2px dashed #cda0d1}
.step{left:572px;width:58px;height:58px;border-radius:50%;background:#fff;border:1.5px solid #cda0d1;font-family:"Yanone Kaffeesatz",sans-serif;font-size:26px;color:var(--purple);text-align:center;line-height:54px}
.reason-photo{border-radius:0 0 0 0}
.reason h3{font-size:21px;font-weight:400;margin-bottom:20px}
.reason p{font-size:12px;line-height:20px;color:#666;margin-bottom:14px}
.reason{width:380px}
.reason.right{text-align:right}
.bonus{left:190px;top:3540px;width:820px;height:248px;border:2px dashed #b77bbd;border-radius:12px;background:var(--lilac);text-align:center;padding:56px 80px 0}
.bonus h3{font-size:22px;font-weight:400;margin-bottom:22px}
.bonus p{font-size:12px;line-height:21px;color:#555}
.bonus-dot{left:595px;top:3534px;width:12px;height:12px;border-radius:50%;background:var(--purple)}

/* shop */
.shop{left:0;top:3897px;width:1200px;height:863px;background:linear-gradient(#fdf0ef,#fbe6e6)}
.course{width:482px;height:136px;background:#fff;border-radius:6px 6px 6px 60px;overflow:hidden}
.course-photo{position:absolute;left:0;top:0;width:140px;height:136px;border-radius:0 0 0 60px}
.price{position:absolute;left:88px;top:16px;padding:2px 8px;background:var(--purple);color:#fff;font-size:12px;border-radius:2px}
.stars{position:absolute;left:58px;top:100px;font-size:13px;color:#f3c74a;letter-spacing:1px}
.course h4{position:absolute;left:166px;top:20px;font-size:14px;font-weight:500}
.course p{position:absolute;left:166px;top:54px;width:290px;font-size:12px;line-height:18px;color:#777}
.course p b{color:var(--purple);font-weight:500}
.buy{position:absolute;left:166px;top:96px;width:104px;height:28px;line-height:28px;font-size:12px;border-radius:14px}
.learn{position:absolute;left:286px;top:96px;width:96px;height:28px;line-height:28px;font-size:12px;border-radius:14px;background:var(--pink-soft);color:#888;text-align:center}
.load{left:476px;top:4597px;width:246px;height:44px;border:1.5px solid var(--purple);border-radius:22px;text-align:center;line-height:41px;font-size:15px;background:#fff}

/* footer */
.footer{left:0;top:4760px;width:1200px;height:350px;background:var(--footer);color:#ddd}
.footer .brand{position:absolute;left:108px;top:110px}
.footer .brand-name{color:#fff;font-size:20px}
.footer .brand-dot{background:#fff;width:30px;height:30px}
.f-head{position:absolute;top:104px;font-family:"Yanone Kaffeesatz",sans-serif;font-size:18px;letter-spacing:1px;color:#fff}
.f-head::after{content:"";position:absolute;left:0;top:28px;width:90px;height:1px;background:#777}
.f-link{position:absolute;font-size:14px;color:#ddd}
.copy{left:0;top:308px;width:1200px;text-align:center;font-size:11px;color:#bbb}
.copy u{color:#eee}
</style>
</head>
<body>

<!-- top bar -->
<div class="abs topbar">
  <span style="left:826px">About</span>
  <span class="sep" style="left:880px"></span>
  <span style="left:904px">Policies</span>
  <span style="left:1040px">◍ Login</span>
</div>

<!-- navigation -->
<header class="abs nav">
  <div class="brand"><span class="brand-dot"></span><span class="brand-name">Quillory Points</span></div>
  <span class="nav-link active" style="left:518px">Home</span>
  <span class="nav-link" style="left:596px">Courses</span>
  <span class="nav-link" style="left:689px">Guidelines</span>
  <span class="nav-link" style="left:800px">FAQs</span>
  <span class="btn-outline">Contact</span>
  <span class="cart"></span>
</header>

<!-- hero -->
<section class="abs hero">
  <svg class="abs" style="left:0;top:0" width="1200" height="554" viewBox="0 0 1200 554">
    <defs>
      <linearGradient id="heroPhoto" x1="0" y1="0" x2="1" y2="1">
        <stop offset="0" stop-color="#e9c6b4"/>
        <stop offset=".5" stop-color="#d7a487"/>
        <stop offset="1" stop-color="#f1e7e3"/>
      </linearGradient>
    </defs>
    <path d="M560 0 H1200 V554 H520 C620 420 640 250 560 0 Z" fill="url(#heroPhoto)" role="img" aria-label="Photo of a woman relaxing during a back massage with a lily in her hair"/>
    <path d="M680 0 C640 120 700 250 600 554 L575 554 C680 260 610 120 650 0 Z" fill="#8f3a97"/>
  </svg>
  <div class="abs hero-kicker">Committed To Excellence In</div>
  <h1 class="abs display hero-title">Massage Therapy<br>Continuing Education</h1>
  <div class="abs search-label">SEARCH ONLINE COURSES</div>
  <div class="abs search">
    <div class="field keyword">Search by Keyword</div>
    <div class="field hours">Number of CE Hours
      <span class="chev"><svg width="12" height="8" viewBox="0 0 12 8"><path d="M1 1l5 5 5-5" fill="none" stroke="#8f3a97" stroke-width="2"/></svg></span>
    </div>
    <div class="btn-search">SEARCH</div>
  </div>
</section>

<!-- popular packages -->
<h2 class="abs display sec-title" style="top:762px">Popular Packages</h2>
<div class="abs divider" style="top:825px"><i></i></div>

<article class="abs pkg" style="left:105px">
  <div class="pkg-photo" role="img" aria-label="Photo of a pregnant woman receiving a massage" style="background:linear-gradient(135deg,#f3e6dc,#d9b49e)"></div>
  <span class="pkg-icon"></span>
  <h3>Pregnancy / Doula</h3>
  <p>Courses And Packages To Become Certified In Every Stage Of Childbearing, From Infertility To Infant Massage</p>
  <span class="more">FIND OUT MORE</span>
</article>
<article class="abs pkg" style="left:444px">
  <div class="pkg-photo" role="img" aria-label="Photo of a Florida city skyline at dusk" style="background:linear-gradient(180deg,#8c7fb4,#e8a884 55%,#3f6a3c)"></div>
  <span class="pkg-icon"></span>
  <h3>Florida Laws &amp; Packages</h3>
  <p>Courses And Packages Required To Obtain, Reinstate, Or Renew Your Florida Massage Therapy License</p>
  <span class="more">FIND OUT MORE</span>
</article>
<article class="abs pkg" style="left:781px">
  <div class="pkg-photo" role="img" aria-label="Photo of a therapist studying on a laptop" style="background:linear-gradient(135deg,#eef0ef,#c9d3cd)"></div>
  <span class="pkg-icon"></span>
  <h3>Research Courses</h3>
  <p>Courses Approved By The NBCEB To Earn Mandated Research Hours For Board Certification Renewal</p>
  <span class="more">FIND OUT MORE</span>
</article>

<!-- free course band -->
<section class="abs band">
  <svg class="abs" style="left:0;top:0" width="1200" height="577" viewBox="0 0 1200 577">
    <defs>
      <linearGradient id="bandPhoto" x1="0" y1="0" x2="1" y2="0">
        <stop offset="0" stop-color="#d9a98e"/>
        <stop offset=".6" stop-color="#f1dfd6"/>
        <stop offset="1" stop-color="#ffffff"/>
      </linearGradient>
      <linearGradient id="bandFade" x1="0" y1="0" x2="1" y2="0">
        <stop offset="0" stop-color="#fff" stop-opacity="0"/>
        <stop offset=".35" stop-color="#fff"/>
      </linearGradient>
    </defs>
    <rect x="0" y="60" width="760" height="517" fill="url(#bandPhoto)" role="img" aria-label="Photo of a hot stone back massage with towels and a white lily"/>
    <rect x="560" y="60" width="640" height="517" fill="url(#bandFade)"/>
    <path d="M0 0 C120 40 200 80 300 110 C230 60 120 30 0 10 Z" fill="#8f3a97"/>
    <path d="M0 70 L0 0 C200 90 420 170 620 130 C800 95 1000 40 1200 80 L1200 60 C1000 20 820 70 620 100 C420 130 200 60 0 0" fill="#f7e4f6"/>
    <path d="M640 110 C820 60 1000 30 1200 70 L1200 80 C1000 50 830 80 660 112 Z" fill="#8f3a97"/>
  </svg>
</section>
<h2 class="abs display band-title">Take a <em>FREE</em> Course</h2>
<p class="abs band-sub">Click here to get started today &amp; try our FREE online course!</p>
<span class="abs btn band-btn">Get a FREE Course</span>

<!-- reasons -->
<div class="abs kicker" style="top:2118px">3 Reasons Why The Quillory Points Offers</div>
<h2 class="abs display sec-title" style="top:2145px;line-height:54px">The Best Online Continuing<br>Education Experience</h2>
<div class="abs divider" style="top:2273px"><i></i></div>

<div class="abs timeline"></div>
<span class="abs step" style="top:2396px">1.</span>
<span class="abs step" style="top:2777px">2.</span>
<span class="abs step" style="top:3162px">3.</span>

<svg class="abs" style="left:165px;top:2380px" width="380" height="313" viewBox="0 0 380 313" role="img" aria-label="Photo of a tablet showing an online education page">
  <path d="M0 0 H300 C350 0 380 40 380 90 V313 H80 C30 313 0 270 0 220 Z" fill="#8f3a97"/>
  <path d="M0 0 H290 C335 0 365 40 365 90 V300 H80 C35 300 0 260 0 220 Z" fill="#b7aa9a"/>
</svg>
<div class="abs reason" style="left:672px;top:2412px">
  <h3>Instant Access And Results</h3>
  <p>Simply enroll in any of our online continuing education courses and you will have instant access to your course. As soon as you pass your test, you can print your certificate instantly. You can have a certificate in your hand tonight.</p>
  <p>There are no delays waiting to receive materials or completion certificates by mail or even by email. After you finish a course, you can always log back into your account, review the course materials, review your exam results, and print additional certificates.</p>
</div>

<div class="abs reason right" style="left:148px;top:2793px">
  <h3>Hassle-Free</h3>
  <p>With our online courses, you work at your own pace. Fit your CEUs into your independent lifestyle. You can log in and out as much as you like while taking a course.</p>
  <p>When you log back in, the system will remember where you last left off, but you can always navigate forward or backward in the course materials if you want to skip ahead or review. Even after you have completed the exam, you will always have access to review the course materials.</p>
</div>
<svg class="abs" style="left:656px;top:2760px" width="380" height="314" viewBox="0 0 380 314" role="img" aria-label="Photo of a smiling woman writing notes at a laptop">
  <path d="M0 0 H300 C350 0 380 40 380 90 V314 H0 Z" fill="#8f3a97"/>
  <path d="M18 18 H290 C330 18 380 50 380 100 V314 H18 Z" fill="#d8c4b2"/>
</svg>

<svg class="abs" style="left:165px;top:3139px" width="380" height="313" viewBox="0 0 380 313" role="img" aria-label="Photo of a yellow sticky note reading free online course beside a keyboard">
  <path d="M80 0 H380 V313 H80 C30 313 0 280 0 230 V0 Z" fill="#8f3a97"/>
  <path d="M80 14 H365 V300 H80 C35 300 0 270 0 230 V14 Z" fill="#c9c2a8"/>
</svg>
<div class="abs reason" style="left:672px;top:3178px">
  <h3>Risk Free Sample Course</h3>
  <p>Take a free course to see exactly how our system operates. This gives you the peace of mind of knowing what to expect before you commit to any of our courses. Feel free to see how well you do with an online learning and testing format. You can test the course from two perspectives: while you are taking it, and when you are finished with it.</p>
  <p>You will see how you can log in and out during the course and/or navigate through it, and how you have access to course materials, test results, and certificates once you have completed the course.</p>
</div>

<span class="abs bonus-dot"></span>
<div class="abs bonus">
  <h3>And If Those Three Reasons Aren't Enough...</h3>
  <p>Another reason to take our home study continuing education courses: We donate 10% of profits to charitable organizations. By doing business with us, you help to support many valuable organizations. We have made donations to Sunrise Camps for Young Readers, Veterans Homeward Ride, Open Field Games, Harbor Relief Alliance, and many other worthy charities. Thank you for your continued support while together we help these wonderful organizations perform their valuable work.</p>
</div>

<!-- shop -->
<section class="abs shop"></section>
<h2 class="abs display sec-title" style="top:3958px">Shop Our Courses</h2>
<div class="abs divider" style="top:4035px"><i></i></div>

<article class="abs course" style="left:105px;top:4089px">
  <div class="course-photo" role="img" aria-label="Photo of hands massaging a client's abdomen" style="background:linear-gradient(135deg,#e7c4b0,#b98970)"></div>
  <span class="price">$209</span><span class="stars">★★★★★</span>
  <h4>Certified Fertility Massage Therapist</h4>
  <p>The online test for this course contains <b>65</b> multiple choice questions.</p>
  <span class="btn buy">Buy Course</span><span class="learn">Learn more</span>
</article>
<article class="abs course" style="left:615px;top:4089px">
  <div class="course-photo" role="img" aria-label="Photo of a new mother with her baby" style="background:linear-gradient(135deg,#9aa4a8,#4f5a60)"></div>
  <span class="price">$229</span><span class="stars">★★★★★</span>
  <h4>Certified Massage Doula</h4>
  <p>The online test for this course contains <b>80</b> multiple choice questions.</p>
  <span class="btn buy">Buy Course</span><span class="learn">Learn more</span>
</article>
<article class="abs course" style="left:105px;top:4250px">
  <div class="course-photo" role="img" aria-label="Photo of a woman stretching on a mat" style="background:linear-gradient(135deg,#f0e8e3,#c9b5a8)"></div>
  <span class="price">$109</span><span class="stars">★★★★★</span>
  <h4>Anatomy Fascial Lines</h4>
  <p>The online test for this course contains <b>54</b> multiple choice questions.</p>
  <span class="btn buy">Buy Course</span><span class="learn">Learn more</span>
</article>
<article class="abs course" style="left:615px;top:4250px">
  <div class="course-photo" role="img" aria-label="Photo of a deep tissue shoulder massage" style="background:linear-gradient(135deg,#d9ab93,#8e5d47)"></div>
  <span class="price">$109</span><span class="stars">★★★★★</span>
  <h4>Deep Tissue Therapy</h4>
  <p>The online test for this course contains <b>60</b> multiple choice questions.</p>
  <span class="btn buy">Buy Course</span><span class="learn">Learn more</span>
</article>
<article class="abs course" style="left:105px;top:4411px">
  <div class="course-photo" role="img" aria-label="Photo of a client draped with a towel during a facial massage" style="background:linear-gradient(135deg,#e9c3ad,#a86e54)"></div>
  <span class="price">$12</span><span class="stars">★★★★★</span>
  <h4>Draping Your Client (Ethics Standard V)</h4>
  <p>The online test for this course contains <b>10</b> multiple choice questions.</p>
  <span class="btn buy">Buy Course</span><span class="learn">Learn more</span>
</article>
<article class="abs course" style="left:615px;top:4411px">
  <div class="course-photo" role="img" aria-label="Photo of a therapist talking with a client" style="background:linear-gradient(135deg,#cfe0e3,#7fa6ae)"></div>
  <span class="price">$24</span><span class="stars">★★★★★</span>
  <h4>Ethics - Communication</h4>
  <p>The online test for this course contains <b>15</b> multiple choice questions.</p>
  <span class="btn buy">Buy Course</span><span class="learn">Learn more</span>
</article>
<div class="abs load">Load More Courses <span style="color:var(--purple)">⟳</span></div>

<div class="abs" role="img" aria-label="Photo of spa items with palm leaves and a mortar of bath salts" style="left:930px;top:4560px;width:270px;height:240px;background:radial-gradient(ellipse at 60% 60%,#5f7d4f 0%,#8aa07a 40%,rgba(251,230,230,0) 70%)"></div>

<!-- footer -->
<footer class="abs footer">
  <div class="brand"><span class="brand-dot"></span><span class="brand-name">Quillory Points</span></div>
  <span class="f-head" style="left:494px">QUICK LINKS</span>
  <span class="f-link" style="left:494px;top:150px">Home</span>
  <span class="f-link" style="left:494px;top:178px">About</span>
  <span class="f-link" style="left:494px;top:206px">FAQs</span>
  <span class="f-link" style="left:494px;top:234px">Courses</span>
  <span class="f-link" style="left:582px;top:152px">Guidelines</span>
  <span class="f-link" style="left:582px;top:180px">Policies</span>
  <span class="f-link" style="left:582px;top:208px">Contact</span>
  <span class="f-head" style="left:738px">ACCOUNT</span>
  <span class="f-link" style="left:738px;top:150px">Login</span>
  <span class="f-link" style="left:738px;top:178px">Sign Up</span>
  <div class="abs copy">©Copyright 2022 <u>Quillory Points</u> | All Rights Reserved</div>
</footer>

</body>
</html>
```